Lumokrit alias Jarek hat fantastische Arbeit geleistet. Zeitnahe Kommunikation, zeitnahe Umsetzung des Feedbacks und zeitnahe Bereitstellung des fertigen Projektes. Gerne jederzeit wieder.
Zielgruppe
Onlinemarketing Services für kleine und mittlere Unternehmen, wie z.B. Webseitenbau, Social Media Kampagnen oder Suchmaschinenoptimierung. Zu unseren Kunden gehören Handwerker, Tierärzte, Rechtsanwälte oder Kfz-Meisterbetriebe. Wir bedienen 6.000 Branchen von Aalräucherei bis Zylinderschleiferei, fokussieren uns aber stark auf das Handwerk.
Aufgabenstellung
Wir planen unsere Produkte unseren Kunden auf einer Plattform zur Verfügung zustellen. Hier sollen sie sich einloggen können und die Self und Managed Services nutzen können. Wir benötigen dafür eine Visualisierung. Also keine echte Webseite, sondern eine Anmutung. Sie soll nicht klickbar sein, aber sich schon wie eine fertige Webseite anfühlen.
Insgesamt sollen 3 Unterseiten gestaltet werden, die wir bereits skizziert (siehe Mockups) haben. Wir sind offen für deine Gestaltungsideen, Hauptsache es sieht nach was aus. Uns ist zudem wichtig, dass du dich bei der Farbgestaltung an der Webseite www.falvoria.com orientierst (Faust-Icon, Logo und Farbe).

```html
<!DOCTYPE html>
<html lang="de">
<head>
<meta charset="utf-8">
<title>falvoria.com Cockpit</title>
<link href="https://fonts.googleapis.com/css2?family=Fira+Sans:wght@500;600&family=Open+Sans:wght@400;600;700&display=swap" rel="stylesheet">
<style>
:root{
  --orange:#ef7d00;
  --ink:#222;
  --grey:#777;
  --muted:#999;
  --panel:#f0f0f0;
  --side:#e6e6e6;
  --card:#fff;
  --line:#c9c9c9;
  --green:#2fb344;
  --blue:#4636ee;
  --red:#f03a2e;
  --yellow:#f7b500;
}
*{box-sizing:border-box;margin:0;padding:0}
html,body{width:860px;height:1200px;overflow:hidden}
body{position:relative;background:#f8f8f8;font-family:"Open Sans",sans-serif;color:var(--ink)}
.abs{position:absolute}

/* header */
.brand{left:68px;top:10px;display:flex;align-items:center;gap:7px}
.brand-dot{width:32px;height:32px;border-radius:50%;background:var(--orange)}
.brand-name{font-family:"Open Sans",sans-serif;font-weight:600;font-size:20px;color:#3a3a3a}
.quick{left:559px;top:20px;width:147px;height:18px;border-radius:9px;background:var(--orange);color:#fff;font-size:8.5px;font-weight:600;display:flex;align-items:center;justify-content:center}
.greeting{left:729px;top:23px;font-size:8.5px;color:#333}
.avatar-m{left:786px;top:20px;width:18px;height:18px;border-radius:50%;background:var(--orange);color:#fff;font-size:10px;display:flex;align-items:center;justify-content:center}

/* sidebar */
.sidebar{left:0;top:56px;width:179px;height:1144px;background:linear-gradient(#e2e2e2,#f2f2f2)}
.nav-item{position:absolute;left:20px;font-size:11.2px;color:#888;letter-spacing:.2px;display:flex;align-items:center;gap:7px;transform:translateY(-50%)}
.nav-item b{color:var(--orange);font-weight:700;font-size:14px;width:9px;text-align:center}
.nav-rule{position:absolute;left:10px;width:159px;height:1px;background:#c4c4c4}
.sub{position:absolute;left:48px;font-size:8.4px;color:#888;transform:translateY(-50%)}
.sub::before{content:"•";position:absolute;left:-8px}

/* panels */
.panel{left:191px;width:614px;background:var(--panel)}
.heading{position:absolute;left:12px;font-family:"Fira Sans",sans-serif;font-weight:600;font-size:19px;color:var(--orange)}
.card{position:absolute;background:var(--card);box-shadow:0 1px 2px rgba(0,0,0,.25)}
.card-label{position:absolute;left:9px;top:7px;font-size:7.8px;color:#222}
.dots{position:absolute;right:10px;top:4px;font-size:10px;color:#aaa;letter-spacing:1px}

/* news */
.news-photo{position:absolute;left:0;top:0}
.news-title{font-weight:700;color:#777;line-height:1.25}
.news-body{color:#999;line-height:1.3;margin-top:8px}

/* calendar */
.cal-grid{position:absolute;font-size:10px;text-align:center}
.cal-grid span{position:absolute;width:20px;margin-left:-10px;transform:translateY(-50%)}
.today{color:#fff;background:var(--orange);border-radius:50%;height:16px;line-height:16px}
.mark{position:absolute;width:3px;height:3px;border-radius:50%}
.events{position:absolute;left:23px;top:877px;font-size:7.6px;color:#999;line-height:9.7px}
.events td{padding-right:8px;white-space:nowrap}
.events td:first-child{font-weight:700;color:#888}

/* chat */
.bubble{position:absolute;top:700px;width:105px;height:89px;background:#e8e8e8;border-radius:8px 8px 8px 0;padding:8px;font-size:7.4px;color:#999;line-height:9.5px}
.person{position:absolute;top:796px;display:flex;gap:6px;align-items:center;font-size:7.6px;line-height:11px}
.person i{display:block;width:24px;height:24px;border-radius:50%;background:linear-gradient(135deg,#9a8678,#3b332e)}
.person small{color:#999;font-size:7.6px}

/* reviews */
.review-btn{position:absolute;left:23px;top:109px;width:91px;height:18px;border:1.3px solid #222;border-radius:9px;font-size:8.6px;display:flex;align-items:center;justify-content:center;letter-spacing:.3px}
</style>
</head>
<body>

<header>
  <div class="abs brand"><span class="brand-dot"></span><span class="brand-name">falvoria.com Cockpit</span></div>
  <div class="abs quick">Schnellanfrage stellen!</div>
  <div class="abs greeting">Hallo Jonas!</div>
  <div class="abs avatar-m">M</div>
</header>

<nav class="abs sidebar">
  <div class="nav-item" style="top:34px"><b>+</b>Cockpit</div>
  <div class="nav-rule" style="top:48px"></div>
  <div class="nav-item" style="top:61px"><b>–</b>Branchen-News</div>
  <div class="sub" style="top:78px">Recht</div>
  <div class="sub" style="top:90px">Steuern</div>
  <div class="sub" style="top:102px">Personal</div>
  <div class="sub" style="top:114px">Marketing</div>
  <div class="sub" style="top:126px">...</div>
  <div class="nav-rule" style="top:144px"></div>
  <div class="nav-item" style="top:156px"><b>+</b>Berichte</div>
  <div class="nav-rule" style="top:169px"></div>
  <div class="nav-item" style="top:183px"><b>+</b>Chat</div>
  <div class="nav-rule" style="top:195px"></div>
  <div class="nav-item" style="top:210px"><b>+</b>Buchungen</div>
  <div class="nav-rule" style="top:223px"></div>
  <div class="nav-item" style="top:236px"><b>+</b>Unternehmen</div>
  <div class="nav-rule" style="top:250px"></div>
  <div class="nav-item" style="top:263px"><b>+</b>Online-Profile</div>
  <div class="nav-rule" style="top:277px"></div>
  <div class="nav-item" style="top:290px"><b>+</b>Bewertungen</div>
  <div class="nav-rule" style="top:304px"></div>
  <div class="nav-item" style="top:317px"><b>+</b>Website</div>
  <div class="nav-rule" style="top:330px"></div>
  <div class="nav-item" style="top:343px"><b>+</b>SEO</div>
  <div class="nav-rule" style="top:356px"></div>
  <div class="nav-item" style="top:370px"><b>+</b>Social Media</div>
  <div class="nav-rule" style="top:383px"></div>
  <div class="nav-item" style="top:397px"><b>+</b>SEA</div>
  <div class="nav-rule" style="top:410px"></div>
  <div class="nav-item" style="top:423px"><b>+</b>Newsletter</div>
  <div class="nav-rule" style="top:437px"></div>
  <div class="nav-item" style="top:450px"><b>+</b>Recruiting</div>
  <div class="nav-rule" style="top:465px"></div>
</nav>

<!-- Branchen-News -->
<section class="abs panel" style="top:56px;height:228px">
  <h2 class="heading" style="top:14px">Deine Branchen-News</h2>
</section>
<article class="card" style="left:202px;top:106px;width:289px;height:155px">
  <div class="news-photo" role="img" aria-label="Foto: Handwerker in Arbeitshandschuhen an einem Sicherungskasten" style="width:88px;height:155px;background:linear-gradient(90deg,#d9d9d6,#eeeeec 60%,#b7b9ba)"></div>
  <div style="position:absolute;left:101px;top:12px;width:175px">
    <div class="news-title" style="font-size:11.2px">Lorem ipsum dolor sit amet, consectetuer adipiscing elit. Aenean commodo ligula eget dolor. Aenean massa.</div>
    <div class="news-body" style="font-size:7.5px">Cum sociis natoque penatibus et magnis dis parturient montes, nascetur ridiculus mus. Donec quam felis, ultricies nec, pellentesque eu, pretium quis, sem. Nulla consequat massa quis enim. Donec pede justo, fringilla vel, aliquet nec elputat.</div>
  </div>
</article>
<article class="card" style="left:503px;top:106px;width:139px;height:155px">
  <div class="news-photo" role="img" aria-label="Foto: Bauarbeiter mit Helm und Warnweste an einem Stahlträger" style="width:139px;height:56px;background:linear-gradient(120deg,#ece8e0,#9c8f80 50%,#e0894a)"></div>
  <div style="position:absolute;left:15px;top:67px;width:115px">
    <div class="news-title" style="font-size:7.6px;line-height:9.5px">Cum sociis natoque pena tibus et magnis dis partur.</div>
    <div class="news-body" style="font-size:7.4px;line-height:9.6px">Eascetur ridiculus mus. Donec quam felis, ultricies nec, pellentesque eu, pretium quis, sem. Nulla consequat massa quis.</div>
  </div>
</article>
<article class="card" style="left:653px;top:106px;width:139px;height:155px">
  <div class="news-photo" role="img" aria-label="Foto: Euromünze über einer blauen Gasflamme" style="width:139px;height:56px;background:radial-gradient(ellipse at 50% 80%,#3d63d8,#1d2438 60%,#7a6a55)"></div>
  <div style="position:absolute;left:7px;top:67px;width:126px">
    <div class="news-title" style="font-size:7.6px;line-height:9.5px">Cum sociis natoque penatibus et magn ascetur ridiculus mus.</div>
    <div class="news-body" style="font-size:7.4px;line-height:9.6px">Donec quam felis, ultricies nec, pellentesque eu, pretium quis, sem. Nulla consequat massa quis enim. Donec pede justo, fringilla vel, aliquet nec elputat.</div>
  </div>
</article>

<!-- Berichte -->
<section class="abs panel" style="top:297px;height:300px">
  <h2 class="heading" style="top:15px">Deine Berichte</h2>
</section>
<article class="card" style="left:202px;top:347px;width:289px;height:220px">
  <div style="position:absolute;left:17px;top:11px;font-size:11px;font-weight:600;color:#777">Lorem ipsum dolor sit amet</div>
  <div class="dots">···</div>
  <svg width="289" height="220" viewBox="0 0 509 387" style="position:absolute;left:0;top:0">
    <g font-family="Open Sans, sans-serif" font-size="13" fill="#222">
      <circle cx="40" cy="79" r="6" fill="var(--red)"/><text x="52" y="84">Restless</text>
      <circle cx="134" cy="79" r="6" fill="var(--yellow)"/><text x="146" y="84">Awake</text>
      <circle cx="217" cy="79" r="6" fill="var(--green)"/><text x="229" y="84">Deep</text>
      <circle cx="294" cy="79" r="6" fill="var(--blue)"/><text x="306" y="84">Time</text>
    </g>
    <g fill="none" stroke-width="1.8" stroke-linejoin="round">
      <polyline stroke="var(--red)" points="33,317 172,233 196,183 302,173 370,194 421,148 476,121"/>
      <polyline stroke="var(--yellow)" points="33,317 102,265 128,276 201,242 254,193 345,208 435,195 476,185"/>
      <polyline stroke="var(--green)" points="33,317 81,296 131,296 176,266 202,284 263,210 342,240 421,164 455,178 476,136"/>
      <polyline stroke="var(--blue)" points="33,317 132,286 237,202 331,266 476,109"/>
    </g>
  </svg>
</article>

<article class="card" style="left:503px;top:347px;width:139px;height:105px">
  <div class="card-label">Webseite</div>
  <svg width="139" height="105" viewBox="0 0 244 185" style="position:absolute;left:0;top:0">
    <circle cx="122" cy="106" r="62" fill="#e6f8df"/>
    <circle cx="122" cy="106" r="58" fill="none" stroke="var(--green)" stroke-width="8" stroke-linecap="round" pathLength="100" stroke-dasharray="67 100" transform="rotate(-90 122 106)"/>
    <text x="122" y="113" text-anchor="middle" font-family="Open Sans, sans-serif" font-weight="700" font-size="19">67%</text>
  </svg>
</article>
<article class="card" style="left:653px;top:347px;width:139px;height:105px">
  <div class="card-label">Findora</div>
  <svg width="139" height="105" viewBox="0 0 244 185" style="position:absolute;left:0;top:0">
    <circle cx="122" cy="106" r="62" fill="#dcdafc"/>
    <circle cx="122" cy="106" r="58" fill="none" stroke="var(--blue)" stroke-width="8" stroke-linecap="round" pathLength="100" stroke-dasharray="46 100" transform="rotate(-90 122 106)"/>
    <text x="122" y="113" text-anchor="middle" font-family="Open Sans, sans-serif" font-weight="700" font-size="19">46%</text>
  </svg>
</article>
<article class="card" style="left:503px;top:462px;width:139px;height:105px">
  <div class="card-label">Socialo</div>
  <svg width="139" height="105" viewBox="0 0 244 185" style="position:absolute;left:0;top:0">
    <circle cx="122" cy="106" r="62" fill="#fde3d6"/>
    <circle cx="122" cy="106" r="58" fill="none" stroke="var(--red)" stroke-width="8" stroke-linecap="round" pathLength="100" stroke-dasharray="22 100" transform="rotate(-90 122 106)"/>
    <text x="122" y="113" text-anchor="middle" font-family="Open Sans, sans-serif" font-weight="700" font-size="19">-15%</text>
  </svg>
</article>
<article class="card" style="left:653px;top:462px;width:139px;height:105px">
  <div class="card-label">Pictura</div>
  <svg width="139" height="105" viewBox="0 0 244 185" style="position:absolute;left:0;top:0">
    <circle cx="122" cy="106" r="62" fill="#d6f8fa"/>
    <circle cx="122" cy="106" r="58" fill="none" stroke="var(--green)" stroke-width="8" stroke-linecap="round" pathLength="100" stroke-dasharray="67 100" transform="rotate(-90 122 106)"/>
    <text x="122" y="113" text-anchor="middle" font-family="Open Sans, sans-serif" font-weight="700" font-size="19">67%</text>
  </svg>
</article>

<!-- Nachrichten -->
<section class="abs panel" style="top:610px;height:341px">
  <h2 class="heading" style="top:15px">Deine Nachrichten</h2>
</section>
<article class="card" style="left:203px;top:661px;width:276px;height:267px">
  <div class="card-label" style="left:19px;top:10px">Webseite</div>
  <div class="dots">···</div>
  <div style="position:absolute;left:0;width:100%;top:32px;text-align:center;font-size:11px;color:#888">
    <span style="color:#222;margin-right:12px">←</span>August 22<span style="color:#222;margin-left:12px">→</span>
  </div>
  <div style="position:absolute;left:17px;top:68px;width:236px;height:1px;background:#eee"></div>
  <div style="position:absolute;left:17px;top:206px;width:236px;height:2px;background:#ddd"></div>
</article>
<div class="cal-grid" style="left:203px;top:0;color:#aaa;font-size:10.5px">
  <span style="left:41px;top:720px">Mo</span><span style="left:71px;top:720px">Di</span><span style="left:102px;top:720px">Mi</span><span style="left:133px;top:720px">Do</span><span style="left:164px;top:720px">Fr</span><span style="left:194px;top:720px">Sa</span><span style="left:225px;top:720px">So</span>
</div>
<div class="cal-grid" style="left:203px;top:0">
  <span style="left:38px;top:748px;color:#888">25</span><span style="left:70px;top:748px;color:#888">26</span><span style="left:101px;top:748px;color:#888">27</span><span style="left:133px;top:748px;color:#888">28</span><span style="left:164px;top:748px">1</span><span style="left:196px;top:748px">2</span><span style="left:228px;top:748px">3</span>
  <span style="left:38px;top:772px">4</span><span style="left:70px;top:772px">5</span><span style="left:101px;top:772px">6</span><span style="left:133px;top:772px">7</span><span style="left:164px;top:772px">8</span><span style="left:196px;top:772px">9</span><span style="left:228px;top:772px">10</span>
  <span style="left:38px;top:797px">11</span><span style="left:70px;top:797px">12</span><span style="left:101px;top:797px">13</span><span style="left:133px;top:797px">14</span><span style="left:164px;top:797px">15</span><span class="today" style="left:196px;top:797px;width:16px;margin-left:-8px">16</span><span style="left:228px;top:797px">17</span>
  <span style="left:38px;top:820px">18</span><span style="left:70px;top:820px">19</span><span style="left:101px;top:820px">20</span><span style="left:133px;top:820px">21</span><span style="left:164px;top:820px">22</span><span style="left:196px;top:820px">23</span><span style="left:228px;top:820px">24</span>
  <span style="left:38px;top:845px">25</span><span style="left:70px;top:845px">26</span><span style="left:101px;top:845px">27</span><span style="left:133px;top:845px">28</span><span style="left:164px;top:845px">29</span><span style="left:196px;top:845px">30</span><span style="left:228px;top:845px">31</span>
</div>
<i class="mark" style="left:369px;top:741px;background:var(--green)"></i>
<i class="mark" style="left:307px;top:765px;background:var(--orange)"></i>
<i class="mark" style="left:342px;top:814px;background:var(--orange)"></i>
<table class="events" style="left:226px">
  <tr><td>23.08.</td><td>14 - 14:30 Uhr</td><td>Nepomuck estas regare esa re</td></tr>
  <tr><td>24.08.</td><td>07 - 07:30 Uhr</td><td>Justase congare neva es</td></tr>
  <tr><td>24.08.</td><td>12 - 12:30 Uhr</td><td>Perola trase nega</td></tr>
  <tr><td>25.08.</td><td>19 - 19:30 Uhr</td><td>Welave tresta jare testa wern</td></tr>
</table>

<article class="card" style="left:503px;top:661px;width:288px;height:187px">
  <div class="card-label" style="left:18px;top:10px">Chatnachrichten</div>
  <div class="dots">···</div>
</article>
<div class="bubble" style="left:528px">Eascetur ridiculus mus. Donec quam felis, ultricies nec, pellen tesque eu, pretium quis, sem. Nulla conse quat massa quis.</div>
<div class="bubble" style="left:660px">Pellentesque eu, pret ium quis, sem. Nulla consequat massa quis enim. Donec</div>
<div class="person" style="left:530px"><i role="img" aria-label="Profilfoto von Lena Brandt"></i><div>Lena Brandt<br><small>Betreff</small></div></div>
<div class="person" style="left:660px"><i role="img" aria-label="Profilfoto von Tobias Rein"></i><div>Tobias Rein<br><small>Betreff</small></div></div>

<!-- Bewertungen -->
<section class="abs panel" style="top:965px;height:235px">
  <h2 class="heading" style="top:15px">Deine Bewertungen</h2>
</section>

<svg width="0" height="0" style="position:absolute">
  <defs>
    <g id="review-icon">
      <path d="M 21 17 A 25 25 0 1 0 5 35" fill="none" stroke="#111" stroke-width="3.2" stroke-linecap="round" transform="translate(0 0)"/>
      <polygon points="0,-14 4,-4.5 14,-4.5 6,2 9,12 0,6 -9,12 -6,2 -14,-4.5 -4,-4.5" fill="#111"/>
      <circle cx="24" cy="24" r="13" fill="#111"/>
      <path d="M18 24 l4.5 4.5 l8 -9" fill="none" stroke="#fff" stroke-width="3" stroke-linecap="round" stroke-linejoin="round"/>
    </g>
  </defs>
</svg>

<article class="card" style="left:203px;top:1016px;width:140px;height:145px">
  <div class="card-label" style="left:10px">Neue Bewertung</div>
  <svg width="140" height="100" style="position:absolute;left:0;top:0"><use href="#review-icon" x="63" y="56"/></svg>
  <div class="review-btn">Antworten</div>
</article>
<article class="card" style="left:353px;top:1016px;width:139px;height:145px">
  <div class="card-label" style="left:10px">Neue Bewertung</div>
  <svg width="140" height="100" style="position:absolute;left:0;top:0"><use href="#review-icon" x="63" y="56"/></svg>
  <div class="review-btn">Antworten</div>
</article>
<article class="card" style="left:502px;top:1016px;width:139px;height:145px">
  <div class="card-label" style="left:10px">Neue Bewertung</div>
  <svg width="140" height="100" style="position:absolute;left:0;top:0"><use href="#review-icon" x="63" y="56"/></svg>
  <div class="review-btn">Antworten</div>
</article>
<article class="card" style="left:651px;top:1016px;width:139px;height:145px">
  <div class="card-label" style="left:10px">Neue Bewertung</div>
  <svg width="140" height="100" style="position:absolute;left:0;top:0"><use href="#review-icon" x="63" y="56"/></svg>
  <div class="review-btn">Antworten</div>
</article>

</body>
</html>
```